Daily special re designs for Hospitality Business / Brewery

Need our daily special social images redone - details as follow and examples attached

I am looking to get an Instagram Square, Facebook Event Cover done for the following promotions:

Meat Free Mondays
Tuesday Scnhitty & Beer for $10.48
Wednesdays - $1 Chicken Wings
Thursdays $15 Pizzas
Friday Burger & Beer for $10.48 12-2pm.
Saturday Half Priced Burgers 12-2pm
Sunday $15 Cocktail Jugs & Live Music

Also need a A3 poster of all the deals combined for in venue use and also a newspaper ad 260mm w x 92mm h

```html
<!DOCTYPE html>
<html lang="en">
<head>
<meta charset="UTF-8">
<title>Red Gum Brewing Co – Saturday Half Priced Burgers</title>
<link href="https://fonts.googleapis.com/css2?family=Archivo:wght@700;800&family=Great+Vibes&family=Montserrat:wght@400;700&display=swap" rel="stylesheet">
<style>
  :root {
    --page-cream: #f8e4bd;
    --panel-cream: #f9e3bc;
    --ink: #0d0d0d;
    --brand-green: #0e7a3f;
    --photo-dark: #5a2a1a;
    --photo-mid: #a8562c;
    --photo-warm: #d9a25c;
    --photo-light: #ecd2a4;
  }
  * { margin: 0; padding: 0; box-sizing: border-box; }
  html, body {
    width: 1200px;
    height: 1200px;
    overflow: hidden;
    background: var(--page-cream);
  }
  .promo {
    position: relative;
    width: 1200px;
    height: 1200px;
    background: var(--page-cream);
  }
  .promo-card {
    position: absolute;
    left: 56px;
    top: 56px;
    width: 1088px;
    height: 1088px;
    border-radius: 16px;
    overflow: hidden;
    box-shadow: 0 0 14px rgba(0, 0, 0, 0.28);
  }
  .burger-photo {
    position: absolute;
    inset: 0;
    background:
      radial-gradient(ellipse 340px 420px at 820px 580px, var(--photo-light) 0%, var(--photo-warm) 45%, transparent 75%),
      radial-gradient(ellipse 240px 380px at 1010px 330px, #f0c14a 0%, transparent 70%),
      linear-gradient(160deg, var(--photo-mid) 0%, var(--photo-dark) 70%, #3a1a10 100%);
  }
  .text-panel {
    position: absolute;
    inset: 0;
    width: 1088px;
    height: 1088px;
  }
  .text-panel path { fill: var(--panel-cream); }
  .brand {
    position: absolute;
    left: 102px;
    top: 130px;
    display: flex;
    align-items: center;
    gap: 14px;
    font-family: "Archivo", sans-serif;
    font-weight: 800;
    font-size: 27px;
    letter-spacing: 1px;
    color: var(--ink);
    text-transform: uppercase;
  }
  .brand-dot {
    width: 26px;
    height: 26px;
    border-radius: 50%;
    background: var(--ink);
  }
  .headline-day {
    position: absolute;
    left: 94px;
    top: 290px;
    font-family: "Great Vibes", cursive;
    font-size: 140px;
    line-height: 1;
    color: var(--ink);
  }
  .headline-offer {
    position: absolute;
    left: 94px;
    top: 450px;
    font-family: "Archivo", sans-serif;
    font-weight: 700;
    font-size: 110px;
    line-height: 1;
    letter-spacing: -2px;
    color: var(--brand-green);
  }
  .headline-item {
    position: absolute;
    left: 92px;
    top: 568px;
    font-family: "Archivo", sans-serif;
    font-weight: 800;
    font-size: 112px;
    line-height: 1;
    letter-spacing: -2px;
    color: var(--ink);
  }
  .availability {
    position: absolute;
    left: 94px;
    top: 756px;
    font-family: "Montserrat", sans-serif;
    color: var(--ink);
  }
  .availability-label {
    font-weight: 400;
    font-size: 38px;
    letter-spacing: 2px;
    line-height: 1.3;
  }
  .availability-time {
    font-weight: 700;
    font-size: 38px;
    letter-spacing: 2px;
    line-height: 1.4;
  }
</style>
</head>
<body>
<main class="promo">
  <section class="promo-card">
    <div class="burger-photo" role="img" aria-label="Close-up photo of a sesame-bun burger with tomato, cheese, lettuce and patty on a wooden board, with fries behind"></div>
    <svg class="text-panel" viewBox="0 0 1088 1088" aria-hidden="true">
      <path d="M0 0 H772 C 760 250, 700 620, 560 745 C 430 850, 220 900, 0 928 Z"/>
    </svg>
    <div class="brand"><span class="brand-dot"></span>Red Gum Brewing Co</div>
  </section>
  <h1 class="headline">
    <span class="headline-day">Saturday</span>
    <span class="headline-offer">Half Priced</span>
    <span class="headline-item">BURGERS</span>
  </h1>
  <div class="availability">
    <p class="availability-label">AVAILABLE:</p>
    <p class="availability-time">12:00 - 2:00 PM</p>
  </div>
</main>
</body>
</html>
```